Flyer for Car Detailing Shop

I am opening a detailing shop. I am looking for a nice, easy to read single sided flyer I can hand out at car shows, hang in store windows and to my clients and customers to promote my business. I want it a little professional yet attention grabbing. I want someone to look at it and go "holy shit, thats a nice flyer" haha

Here are some things that must be included:
- Company Name: Brightfern Motorworks Detailing & Coatings
- Tag Line: The Science of Detailing
- Address: 4150 Harlow Rd, Temperance, MI 48190
- www.brightfernmotor.example
- Find Us on social Media! ::insert facebook and instagram logo
Colors: Black, Lime Green and Purple for accents, etc

HAND WASH
- Express Wash start at $25
- Deluxe Wash Start at $50

EXTERIOR DETAILING
-Basic Packages Start at $160
- Deluxe Packages Start at $350

INTERIOR DETAILING
- Basic Packages Start at $60
- Deluxe Packages Start at $200

New Car Prep and Ceramic Coatings
*Consultation required prior to beginning work*
- Paint: Starting at $500
- Interior: Starting at $100
- Wheels Off: Starting at $200
- Trim: Starting at $100
- Windows: $50 windshield/ $25 per pane

Additional Services
- Scratch removal
- Ozone Treatment
- Headlight Restoration
- Chip Repair

```html
<!DOCTYPE html>
<html lang="en">
<head>
<meta charset="utf-8">
<title>Brightfern Motorworks Detailing &amp; Coatings – Flyer</title>
<link rel="stylesheet" href="https://fonts.googleapis.com/css2?family=Arimo:wght@700&family=Lato:wght@400;700&display=swap">
<style>
  :root{
    --page:#e4e0da;
    --ink:#111214;
    --panel:#333435;
    --white:#ffffff;
    --lime:#4cc43c;
    --purple:#7a1689;
    --muted:#d9d9d9;
  }
  *{box-sizing:border-box;margin:0;padding:0}
  html,body{width:1200px;height:1200px;overflow:hidden;background:var(--page)}
  .flyer{position:absolute;left:200px;top:36px;width:800px;height:1127px;background:var(--ink);overflow:hidden;font-family:"Lato",sans-serif;color:var(--white)}
  .hero-photo{position:absolute;left:0;top:0;width:800px;height:1040px;
    background:
      radial-gradient(ellipse 260px 200px at 22% 48%,rgba(150,160,175,.55),transparent 70%),
      radial-gradient(ellipse 300px 380px at 80% 45%,rgba(150,110,85,.45),transparent 70%),
      radial-gradient(ellipse 200px 160px at 88% 12%,rgba(200,80,40,.45),transparent 70%),
      linear-gradient(180deg,#15161a 0%,#23252b 45%,#121316 75%,#0e0f11 100%)}
  .brand{position:absolute;left:0;width:800px;top:58px;text-align:center;font-family:"Lato",sans-serif;font-weight:700;color:var(--white)}
  .brand-mark{width:46px;height:46px;border-radius:50%;background:var(--white);margin:0 auto 16px}
  .brand-name{font-size:32px;line-height:1.1;letter-spacing:.5px}
  .brand-sub{font-size:11px;letter-spacing:3px;margin-top:8px;text-transform:uppercase}
  .footer-band{position:absolute;left:0;top:1037px;width:800px;height:90px;background:var(--purple)}
  .menu-panel{position:absolute;left:20px;top:597px;width:760px;height:468px;background:var(--panel);border:2px solid var(--white);border-radius:52px 52px 0 0}
  .headline{position:absolute;left:0;width:800px;text-align:center;top:626px;font-family:"Arimo",sans-serif;font-weight:700;font-size:50px;line-height:62px;white-space:nowrap;letter-spacing:-.3px}
  .accent{color:var(--lime)}
  .section-title{position:absolute;font-family:"Arimo",sans-serif;font-weight:700;font-size:18.5px;line-height:22px;white-space:nowrap}
  .section-title::after{content:"";position:absolute;left:0;top:28px;width:31px;height:3px;background:var(--lime)}
  .price-list{position:absolute;list-style:none;font-size:16px;line-height:24px;white-space:nowrap}
  .price-list.bulleted li::before{content:"";display:inline-block;width:7px;height:7px;border-radius:50%;background:var(--lime);margin-right:6px;vertical-align:2px}
  .price-list b{font-weight:700}
  .divider{position:absolute;left:320px;top:729px;width:2px;height:307px;background:var(--lime)}
  .consult-note{position:absolute;left:362px;top:752px;font-size:12px;font-weight:700;color:var(--muted);white-space:nowrap}
  .extras-badge{position:absolute;left:360px;top:921px;width:246px;height:34px;border-radius:10px;background:var(--lime);font-family:"Arimo",sans-serif;font-weight:700;font-size:18.5px;line-height:34px;text-align:center}
  .extra-item{position:absolute;top:972px;width:110px;margin-left:-55px;text-align:center;font-size:16px;line-height:19px}
  .extra-item svg{display:block;margin:0 auto 6px}
  .contact{position:absolute;top:1087px;font-size:13.5px;line-height:20px;white-space:nowrap;display:flex;align-items:center;gap:10px}
  .social-dot{width:26px;height:26px;border-radius:50%;background:var(--lime);display:inline-block}
</style>
</head>
<body>
<main class="flyer">
  <div class="hero-photo" role="img" aria-label="Photo of a detailer in a respirator polishing the headlight area of a dark car with a rotary buffer"></div>

  <div class="brand">
    <div class="brand-mark"></div>
    <div class="brand-name">Brightfern Motorworks</div>
    <div class="brand-sub">Detailing &amp; Coatings</div>
  </div>

  <div class="footer-band"></div>
  <section class="menu-panel"></section>

  <h1 class="headline">THE SCIENCE OF <span class="accent">DETAILING</span></h1>

  <h2 class="section-title" style="left:52px;top:718px"><span class="accent">HAND</span> WASH</h2>
  <ul class="price-list bulleted" style="left:52px;top:757px">
    <li>Express Wash start at <b>$25</b></li>
    <li>Deluxe Wash Start at <b>$50</b></li>
  </ul>

  <h2 class="section-title" style="left:52px;top:837px"><span class="accent">EXTERIOR</span> DETAILING</h2>
  <ul class="price-list bulleted" style="left:52px;top:875px">
    <li>Basic Packages Start at <b>$160</b></li>
    <li>Deluxe Packages Start at <b>$350</b></li>
  </ul>

  <h2 class="section-title" style="left:52px;top:952px"><span class="accent">INTERIOR</span> DETAILING</h2>
  <ul class="price-list bulleted" style="left:52px;top:991px">
    <li>Basic Packages Start at <b>$60</b></li>
    <li>Deluxe Packages Start at <b>$200</b></li>
  </ul>

  <div class="divider"></div>

  <h2 class="section-title" style="left:362px;top:713px"><span class="accent">NEW</span> CAR PREP AND CERAMIC COATINGS</h2>
  <p class="consult-note">*Consultation required prior to beginning work*</p>
  <ul class="price-list" style="left:362px;top:772px">
    <li>Paint: Starting at <b>$500</b></li>
    <li>Interior: Starting at <b>$100</b></li>
    <li>Wheels Off: Starting at <b>$200</b></li>
    <li>Trim: Starting at <b>$100</b></li>
    <li>Windows: $50 windshield/ <b>$25 per pane</b></li>
  </ul>

  <div class="extras-badge">ADDITIONAL SERVICES</div>

  <div class="extra-item" style="left:393px"><svg width="22" height="18" viewBox="0 0 22 18"><path d="M2 9l6 6L20 2" fill="none" stroke="#4cc43c" stroke-width="4"/></svg>Scratch<br>removal</div>
  <div class="extra-item" style="left:506px"><svg width="22" height="18" viewBox="0 0 22 18"><path d="M2 9l6 6L20 2" fill="none" stroke="#4cc43c" stroke-width="4"/></svg>Ozone<br>Treatment</div>
  <div class="extra-item" style="left:618px"><svg width="22" height="18" viewBox="0 0 22 18"><path d="M2 9l6 6L20 2" fill="none" stroke="#4cc43c" stroke-width="4"/></svg>Headlight<br>Restoration</div>
  <div class="extra-item" style="left:730px"><svg width="22" height="18" viewBox="0 0 22 18"><path d="M2 9l6 6L20 2" fill="none" stroke="#4cc43c" stroke-width="4"/></svg>Chip<br>Repair</div>

  <div class="contact" style="left:24px">
    <svg width="16" height="20" viewBox="0 0 16 20"><path d="M8 1a6 6 0 0 0-6 6c0 4.5 6 11 6 11s6-6.5 6-11a6 6 0 0 0-6-6z" fill="none" stroke="#4cc43c" stroke-width="1.8"/><circle cx="8" cy="7" r="2.2" fill="#4cc43c"/></svg>
    <span>4150 Harlow Rd, Temperance, MI 48190</span>
  </div>
  <div class="contact" style="left:332px">
    <svg width="19" height="19" viewBox="0 0 20 20" fill="none" stroke="#4cc43c" stroke-width="1.6"><circle cx="10" cy="10" r="8.5"/><ellipse cx="10" cy="10" rx="4" ry="8.5"/><path d="M1.5 10h17M3 5.5h14M3 14.5h14"/></svg>
    <span>www.brightfernmotor.example</span>
  </div>
  <div class="contact" style="left:567px;gap:6px">
    <span style="margin-right:8px">Find Us on social Media!</span>
    <span class="social-dot" aria-label="Social profile link"></span>
    <span class="social-dot" aria-label="Social profile link"></span>
  </div>
</main>
</body>
</html>
```